Website Design for Meridel Power Works

We design and install solar power systems for homes and businesses. We also provide engineering services for commercial and utility scale projects

```html
<!DOCTYPE html>
<html lang="en">
<head>
<meta charset="utf-8">
<title>Meridel Power Works</title>
<link href="https://fonts.googleapis.com/css2?family=Open+Sans:wght@300;400;600&display=swap" rel="stylesheet">
<style>
:root{
  --page-bg:#ffffff;
  --header-bg:#ececec;
  --band-light:#ececec;
  --band-stories:#e2e2e2;
  --card-white:#f7f7f7;
  --text-grey:#6a6a6a;
  --text-dark:#555555;
  --green:#6cc040;
  --blue:#5ab6e8;
  --orange:#f9a72e;
  --footer-bg:#666666;
  --footer-text:#d8d8d8;
  --footer-line:#8a8a8a;
  --bottom-bg:#333333;
  --brand-red:#d8442a;
}
*{margin:0;padding:0;box-sizing:border-box}
html,body{width:1200px;height:1196px;overflow:hidden;background:var(--page-bg);font-family:"Open Sans",Arial,sans-serif}
.page{position:absolute;left:164px;top:0;width:868px;height:1196px}
.abs{position:absolute}

/* header */
.site-header{left:0;top:0;width:868px;height:73px;background:var(--header-bg)}
.brand{left:28px;top:20px;display:flex;align-items:center;gap:10px}
.brand-mark{width:28px;height:28px;border-radius:50%;background:var(--brand-red)}
.brand-name{font-size:15px;font-weight:400;color:var(--text-grey);letter-spacing:.5px}
.util-icons{left:762px;top:10px;display:flex;gap:8px}
.phone{right:62px;top:26px;font-size:26px;font-weight:300;color:var(--text-grey)}

/* hero */
.hero{left:0;top:73px;width:868px;height:364px;background:linear-gradient(90deg,#d9cfc2 0%,#f2d6b8 30%,#e9c79a 55%,#d8dfe6 80%,#c9b6a0 100%)}
.thumbs{right:10px;top:10px;display:flex;gap:11px}
.thumb{width:72px;height:60px;border:2px solid #fff;box-shadow:0 1px 3px rgba(0,0,0,.3)}

/* services */
.services{left:0;top:437px;width:868px;height:239px;background:var(--band-light)}
.tile{top:43px;width:244px;height:164px;box-shadow:4px 4px 6px rgba(0,0,0,.15);color:#fff;text-align:center}
.tile h2{font-weight:300;font-size:27px;margin-top:14px;letter-spacing:.3px}
.tile-residential{left:52px;background:var(--green)}
.tile-commercial{left:313px;background:var(--blue)}
.tile-quote{left:575px;background:var(--orange)}
.tile-icon{position:absolute;left:77px;top:56px;width:90px;height:90px;border-radius:50%;background:rgba(255,255,255,.35)}
.field{position:absolute;left:25px;width:192px;height:24px;background:#f4f4f4;border:1px solid #e0e0e0;font-size:9px;color:#bbb;text-align:left;padding:6px 10px}
.field-name{top:52px}
.field-email{top:84px}
.make-request{position:absolute;left:74px;top:123px;width:104px;height:27px;border-radius:3px;background:linear-gradient(#fafafa,#dcdcdc);color:#555;font-size:10px;font-weight:600;line-height:27px;box-shadow:0 1px 2px rgba(0,0,0,.3)}

/* success stories */
.stories{left:0;top:676px;width:868px;height:192px;background:var(--band-stories)}
.story-card{left:103px;top:19px;width:660px;height:149px;background:var(--card-white);box-shadow:0 1px 2px rgba(0,0,0,.12)}
.story-head{height:49px;background:#ededed;border-bottom:1px solid #d6d6d6;text-align:center;font-size:27px;color:var(--text-grey);line-height:49px;font-weight:400}
.quote-mark{font-family:Georgia,serif;font-size:72px;color:#c9c9c9;line-height:1}
.quote-open{left:10px;top:42px}
.quote-close{right:10px;top:86px}
.story-text{left:70px;top:66px;width:540px;font-size:14px;line-height:20px;color:var(--text-dark)}
.story-author{right:70px;top:116px;font-size:10px;color:#aaa}

/* footer */
.footer{left:0;top:868px;width:868px;height:287px;background:var(--footer-bg);color:var(--footer-text)}
.footer h3{position:absolute;font-size:12px;font-weight:400;color:#eee;letter-spacing:.5px}
.footer p{position:absolute;font-size:8.5px;line-height:14.5px}
.about-text{left:73px;top:52px;width:212px}
.client{position:absolute;width:48px;height:48px;border:2px solid #e8e8e8;background:linear-gradient(#d8b89a,#b88f70)}
.nav-link{position:absolute;width:111px;font-size:8.5px;border-bottom:1px solid var(--footer-line);padding-bottom:4px}
.contact-text{left:328px;top:194px;width:210px}
.subscribe-text{left:589px;top:53px;width:210px}
.email-field{position:absolute;left:589px;top:84px;width:184px;height:21px;background:#efefef;color:#888;font-size:8px;padding:4px 6px}
.submit-btn{position:absolute;left:589px;top:113px;width:55px;height:20px;background:#3f3f3f;color:#eee;font-size:8px;text-align:center;line-height:20px;border-radius:2px}
.social-text{left:589px;top:196px;width:200px}
.socials{position:absolute;left:589px;top:232px;display:flex;gap:4px}
.social{width:24px;height:24px;border-radius:50%;border:2px solid #eee}

/* bottom bar */
.bottom-bar{left:0;top:1155px;width:868px;height:41px;background:var(--bottom-bg);color:#ddd;font-size:9px}
.copyright{left:73px;top:14px}
.legal{right:70px;top:14px}
</style>
</head>
<body>
<div class="page">

  <header class="site-header abs">
    <div class="brand abs"><span class="brand-mark"></span><span class="brand-name">MERIDEL POWER WORKS</span></div>
    <div class="util-icons abs">
      <svg width="12" height="12" viewBox="0 0 12 12" aria-label="Home"><path d="M1 6 6 1.5 11 6M2.5 5v6h7V5" fill="none" stroke="#999" stroke-width="1.3"/></svg>
      <svg width="13" height="12" viewBox="0 0 13 12" aria-label="Mail"><rect x="1" y="2" width="11" height="8" fill="none" stroke="#999" stroke-width="1.3"/><path d="M1 2l5.5 4.5L12 2" fill="none" stroke="#999" stroke-width="1.3"/></svg>
      <svg width="28" height="12" viewBox="0 0 28 12" aria-label="Heat"><path d="M1 3q3-2 6 0t6 0 6 0 6 0M1 7q3-2 6 0t6 0 6 0 6 0M1 11q3-2 6 0t6 0 6 0 6 0" fill="none" stroke="#ea6a3a" stroke-width="1.3"/></svg>
    </div>
    <div class="phone abs">Call Us: 02 5550 1927</div>
  </header>

  <section class="hero abs" role="img" aria-label="Smiling family of four with their cat at home">
    <div class="thumbs abs">
      <div class="thumb" role="img" aria-label="Family at home" style="background:linear-gradient(#f2d2a8,#d9a978)"></div>
      <div class="thumb" role="img" aria-label="Business team" style="background:linear-gradient(#cfd6dd,#8f9aa3)"></div>
      <div class="thumb" role="img" aria-label="Solar installers on a roof" style="background:linear-gradient(#8fb6d8,#c08a55)"></div>
      <div class="thumb" role="img" aria-label="Installer working on panels" style="background:linear-gradient(#aab8c3,#b7704a)"></div>
    </div>
  </section>

  <section class="services abs">
    <div class="tile tile-residential abs">
      <h2>RESIDENTIAL</h2>
      <div class="tile-icon">
        <svg width="90" height="90" viewBox="0 0 90 90"><path d="M22 50 45 33 68 50M28 47v14M35 42v19M42 37v24M49 37v24M56 42v19M63 47v14M24 61h42" fill="none" stroke="#fff" stroke-width="2.5"/></svg>
      </div>
    </div>
    <div class="tile tile-commercial abs">
      <h2>COMMERCIAL</h2>
      <div class="tile-icon">
        <svg width="90" height="90" viewBox="0 0 90 90"><path d="M26 64V44h10v20M36 64V26h14v38M50 64V36h12v28M22 64h44M40 34h6M40 42h6M40 50h6" fill="none" stroke="#fff" stroke-width="2.5"/></svg>
      </div>
    </div>
    <div class="tile tile-quote abs">
      <h2>GET FREE QUOTE</h2>
      <div class="field field-name">Name</div>
      <div class="field field-email">Email</div>
      <div class="make-request">MAKE REQUEST</div>
    </div>
  </section>

  <section class="stories abs">
    <div class="story-card abs">
      <div class="story-head">Success Stories</div>
      <div class="quote-mark quote-open abs">&ldquo;</div>
      <p class="story-text abs">Lorem Ipsum is simply dummy text of the printing and typesetting industry. Lorem Ipsum has been the industry's standard dummy text ever since the 1500s</p>
      <div class="story-author abs">- Lena Marsh</div>
      <div class="quote-mark quote-close abs">&rdquo;</div>
    </div>
  </section>

  <footer class="footer abs">
    <h3 style="left:73px;top:27px">ABOUT</h3>
    <p class="about-text">Meridel Power Works (MPW) is an Australian based Renewable Energy services company with core key competencies in solar PV system engineering, design and installation. [...]</p>
    <h3 style="left:73px;top:124px">CLIENTS</h3>
    <div class="client" role="img" aria-label="Client portrait" style="left:72px;top:156px"></div>
    <div class="client" role="img" aria-label="Client portrait" style="left:144px;top:156px"></div>
    <div class="client" role="img" aria-label="Client portrait" style="left:216px;top:156px"></div>
    <div class="client" role="img" aria-label="Client portrait" style="left:72px;top:216px"></div>
    <div class="client" role="img" aria-label="Client portrait" style="left:144px;top:216px"></div>
    <div class="client" role="img" aria-label="Client portrait" style="left:216px;top:216px"></div>

    <h3 style="left:328px;top:27px">NAVIGATION</h3>
    <span class="nav-link" style="left:328px;top:52px">Home</span>
    <span class="nav-link" style="left:440px;top:52px">Business</span>
    <span class="nav-link" style="left:328px;top:76px">About</span>
    <span class="nav-link" style="left:440px;top:76px">FREE Quote</span>
    <span class="nav-link" style="left:328px;top:100px">Projects</span>
    <span class="nav-link" style="left:440px;top:100px">Benefits</span>
    <span class="nav-link" style="left:328px;top:124px">Residential</span>
    <span class="nav-link" style="left:440px;top:124px">Success Stories</span>

    <h3 style="left:328px;top:168px">CONTACT INFO</h3>
    <p class="contact-text">48 Harbourview Lane, Eastmere,<br>Southvale, Australia 2950<br>Email: hello@meridelpower.com.au<br>Website: www.meridelpower.com.au<br>Phone: 02 5550 1927</p>

    <h3 style="left:589px;top:27px">SUBSCRIBE</h3>
    <p class="subscribe-text">Lorem ipsum dolor sit amet, consectetur adipiscing elit. Aenean nisi orci, condimentum.</p>
    <div class="email-field">enter your email address here</div>
    <div class="submit-btn">SUBMIT</div>

    <h3 style="left:589px;top:173px">SOCIAL NETWORKS</h3>
    <p class="social-text">Pellentesque tincidunt erat quam. Donec laoreet consectetur libero non varius.</p>
    <div class="socials">
      <span class="social" style="background:#3b5998"></span>
      <span class="social" style="background:#2fa9e0"></span>
      <span class="social" style="background:#1d87bd"></span>
      <span class="social" style="background:#d9483b"></span>
      <span class="social" style="background:#f0672a"></span>
    </div>
  </footer>

  <div class="bottom-bar abs">
    <span class="copyright abs">Meridel Power 2013 &copy; - All rights reserved.</span>
    <span class="legal abs">Terms &nbsp;|&nbsp; Privacy Policy</span>
  </div>
</div>
</body>
</html>
```